Bookcover: Ways to Turn Into a Bold Pathfinder

I am publishing a super-low-cost innovation book for €4,99 on Pageleaf Open Press to help everyone become a great innovator: young ambitious people without college education nor a big budget. Do you want to help me?

Brief:
Design a book cover 1600 x 2560 pixels for POP.
Main title: Ways to Turn Into a Bold Pathfinder
Sub title: mindset - insights - skills & tools
Author: Maarten de Kolkema
Design: captive, and appealing to everyone
Target Group: young ambitious people without college education

For pageleaf please format the height/width ratio of 1.6:1

```html
<!DOCTYPE html>
<html lang="en">
<head>
<meta charset="utf-8">
<title>Ways to Turn Into a Bold Pathfinder — Book Cover</title>
<link rel="stylesheet" href="https://fonts.googleapis.com/css2?family=Archivo+Black&family=Open+Sans:wght@600&display=swap">
<style>
  :root {
    --stage-light: #e4e4e4;
    --stage-dark: #bdbdbd;
    --teal-light: #22a0a2;
    --teal-mid: #138b8d;
    --teal-dark: #077578;
    --paper: #ffffff;
    --orange: #f7941d;
    --brain-pink: #d9687a;
    --brain-blue: #3f79b5;
    --brain-green: #a7c46a;
    --brain-cream: #e7e0cf;
  }
  * { margin: 0; padding: 0; box-sizing: border-box; }
  html, body {
    width: 1200px;
    height: 738px;
    overflow: hidden;
  }
  body {
    background: radial-gradient(ellipse at 50% 60%, var(--stage-light) 0%, var(--stage-dark) 100%);
    position: relative;
  }
  .book-cover {
    position: absolute;
    left: 380px;
    top: 17px;
    width: 440px;
    height: 704px;
    box-shadow: 0 12px 30px rgba(0, 0, 0, 0.28);
  }
  .book-cover svg { display: block; width: 100%; height: 100%; }
  .title-light {
    font-family: "Open Sans", Arial, sans-serif;
    font-weight: 600;
    fill: var(--orange);
  }
  .title-heavy, .tagline, .author-name {
    font-family: "Archivo Black", "Arial Black", sans-serif;
    fill: var(--orange);
  }
</style>
</head>
<body>
  <main class="book-cover">
    <svg viewBox="0 0 811 1298" xmlns="http://www.w3.org/2000/svg" aria-labelledby="cover-title">
      <title id="cover-title">Ways to Turn Into a Bold Pathfinder by Maarten de Kolkema</title>
      <defs>
        <radialGradient id="teal-field" cx="50%" cy="40%" r="75%">
          <stop offset="0%" stop-color="var(--teal-light)"/>
          <stop offset="55%" stop-color="var(--teal-mid)"/>
          <stop offset="100%" stop-color="var(--teal-dark)"/>
        </radialGradient>
        <linearGradient id="brain-tones" x1="0" y1="0" x2="1" y2="1">
          <stop offset="0%" stop-color="var(--brain-blue)"/>
          <stop offset="40%" stop-color="var(--brain-pink)"/>
          <stop offset="70%" stop-color="var(--brain-green)"/>
          <stop offset="100%" stop-color="var(--brain-cream)"/>
        </linearGradient>
        <filter id="soft-glow" x="-20%" y="-20%" width="140%" height="140%">
          <feGaussianBlur stdDeviation="10"/>
        </filter>
      </defs>

      <rect class="cover-field" width="811" height="1298" fill="url(#teal-field)"/>

      <g class="decor-circles" fill="var(--paper)">
        <circle cx="790" cy="0" r="145"/>
        <circle cx="-77" cy="790" r="285"/>
        <circle cx="735" cy="1205" r="305"/>
      </g>

      <g class="main-title" text-anchor="middle">
        <text class="title-light" x="393" y="83" font-size="90">WAYS TO</text>
        <text class="title-light" x="393" y="183" font-size="90">TURN INTO A</text>
        <text class="title-heavy" x="391" y="283" font-size="82">BOLD</text>
        <text class="title-heavy" x="404" y="413" font-size="124" textLength="732" lengthAdjust="spacingAndGlyphs">PATHFINDER</text>
      </g>

      <g class="subtitle">
        <text class="tagline" x="38" y="461" font-size="46" textLength="217" lengthAdjust="spacingAndGlyphs">MINDSET</text>
        <text class="tagline" x="221" y="551" font-size="46" textLength="227" lengthAdjust="spacingAndGlyphs">INSIGHTS</text>
        <text class="tagline" x="378" y="641" font-size="46" textLength="393" lengthAdjust="spacingAndGlyphs">SKILLS &amp; TOOLS</text>
      </g>

      <g class="cover-illustration" role="img" aria-label="Colourful paper-collage illustration of a human brain seen from the side">
        <ellipse cx="387" cy="850" rx="300" ry="200" fill="#ffffff" opacity="0.45" filter="url(#soft-glow)"/>
        <ellipse cx="387" cy="845" rx="292" ry="185" fill="url(#brain-tones)"/>
      </g>

      <text class="author-name" x="20" y="1143" font-size="48" textLength="385" lengthAdjust="spacingAndGlyphs">MAARTEN DE KOLKEMA</text>
    </svg>
  </main>
</body>
</html>
```